Poster for Office

Looking for an edgy, beautiful poster to hang up in my office that uses the quotes located below and potentially the image attached.
Content for poster

Title: Pell's Rules

Must have the following quotes included (punctuation and capitalization are flexible, do what you think looks the best they also don't need the quotation symbols):

"Don't order fish at a steakhouse"
"Be bold. The more you tell, the more you sell"
"admit nothing, deny everything, launch counterattack."
"avoid obviousness"
"never do anything until you're ready to do it"
"look good=feel good"
"always keep the advantage"
"never complain, never explain"
"Lay low, play dumb, keep moving"

Industry/Entity Type

Quotes

Requirements
Must have
• Title: Pell's Rules

"avoid obviousness"
"look good=feel good"

```html
<!DOCTYPE html>
<html lang="en">
<head>
<meta charset="utf-8">
<title>Pell's Rules</title>
<link rel="stylesheet" href="https://fonts.googleapis.com/css2?family=Anton&family=Archivo+Black&family=Oswald:wght@500;700&display=swap">
<style>
  :root {
    --paper: #ffffff;
    --photo-top: #d2d2d2;
    --photo-bottom: #e4e4e4;
    --blue-title: #2f5cf6;
    --blue-bright: #3563f2;
    --blue-soft: #5d86ee;
    --blue-deep: #1a22c8;
    --blue-sky: #6aa7ef;
    --blue-royal: #2a44d9;
    --blue-lilac: #6a84e4;
    --blue-cyan: #5cb6f4;
    --blue-ink: #1727d6;
  }
  * { margin: 0; padding: 0; box-sizing: border-box; }
  html, body { width: 854px; height: 1200px; overflow: hidden; background: var(--paper); }
  .poster {
    position: relative;
    width: 854px;
    height: 1200px;
    background: var(--paper);
    overflow: hidden;
  }
  .photo-area {
    position: absolute;
    inset: 0;
    background: linear-gradient(180deg, var(--photo-top) 0%, var(--photo-bottom) 100%);
  }
  .line {
    position: absolute;
    left: 0;
    right: 0;
    text-align: center;
    white-space: nowrap;
    line-height: 1;
  }
  .title {
    top: 222px;
    font-family: "Anton", "Archivo Black", sans-serif;
    font-weight: 400;
    font-size: 122px;
    letter-spacing: 2px;
    color: var(--blue-title);
    transform: scaleX(1.24);
    transform-origin: 50% 50%;
  }
  .rule-fish {
    top: 462px;
    font-family: "Oswald", sans-serif;
    font-weight: 700;
    font-size: 52px;
    letter-spacing: 1.4px;
    color: var(--blue-bright);
  }
  .rule-bold {
    top: 538px;
    font-family: "Oswald", sans-serif;
    font-weight: 500;
    font-size: 33px;
    letter-spacing: 3.4px;
    color: var(--blue-soft);
  }
  .rule-admit {
    top: 594px;
    font-family: "Oswald", sans-serif;
    font-weight: 700;
    font-size: 28px;
    letter-spacing: 2px;
    color: var(--blue-deep);
  }
  .rule-obvious {
    top: 632px;
    font-family: "Archivo Black", sans-serif;
    font-size: 64px;
    letter-spacing: 4.6px;
    color: var(--blue-sky);
  }
  .rule-ready {
    top: 716px;
    font-family: "Oswald", sans-serif;
    font-weight: 700;
    font-size: 42px;
    letter-spacing: -0.2px;
    color: var(--blue-royal);
  }
  .rule-look {
    top: 776px;
    font-family: "Archivo Black", sans-serif;
    font-size: 56px;
    letter-spacing: 6px;
    color: var(--blue-lilac);
  }
  .rule-advantage {
    top: 848px;
    font-family: "Archivo Black", sans-serif;
    font-size: 36px;
    letter-spacing: 7.7px;
    color: var(--blue-cyan);
  }
  .rule-complain {
    top: 890px;
    font-family: "Anton", sans-serif;
    font-size: 56px;
    letter-spacing: 1.5px;
    color: var(--blue-bright);
  }
  .rule-lay {
    top: 952px;
    font-family: "Archivo Black", sans-serif;
    font-size: 38px;
    letter-spacing: 2px;
    color: var(--blue-ink);
  }
</style>
</head>
<body>
  <main class="poster">
    <div class="photo-area" role="img" aria-label="Black and white photograph of a man's bare back with a large portrait tattoo between the shoulder blades"></div>

    <h1 class="line title">Pell’s Rules</h1>

    <p class="line rule-fish">Don’t order fish at a steakhouse</p>
    <p class="line rule-bold">Be bold. The more you tell, the more you sell</p>
    <p class="line rule-admit">admit nothing, deny everything, launch counterattack</p>
    <p class="line rule-obvious">avoid obviousness</p>
    <p class="line rule-ready">never do anything until you’re ready to do it</p>
    <p class="line rule-look">look good=feel good</p>
    <p class="line rule-advantage">always keep the advantage</p>
    <p class="line rule-complain">never complain, never explain</p>
    <p class="line rule-lay">lay low, play dumb, keep moving</p>
  </main>
</body>
</html>
```